Cake website needs a professional WordPress design makeover!

I need a wordpress design for my company called Velvet Crumbhouse. It's a home cake business and I specialise in everything from cupcakes, celebratory cakes to couture wedding cakes. I have an existing one page wordpress website www.velvetcrumbhouse.com but it doesn't quite communicate elegance or showcase my skills so it desperately needs a complete change.

I purchased this theme
http://tilecraftery.com/demos/themes/?product=lumo
I basically want my website to look EXACTLY like this. I would obviously provide pictures of my work. I like the positioning of the pictures and texts and how each section are divided with the pictures. I also like the pop up of the welcome text on the home page. I would like that to say Welcome Velvet Crumbhouse.

One element I would like to keep from my original website are the slides on the home page. But will have a different caption with each slide. I will provide the three pictures for these slides.

The page format should be as follows:

Home
Discover Our Story
Tasteful Delights (Picture)
Discover Our Cakes - Clickable link below description going to the full cake menu with prices
The Perfect Blend (Picture)
Our Promise
Discover Your Special Day (Picture)
Wedding Cakes
Make an Order (Picture)
Get in touch

The menu on top of the page should read
Home, Our story, Our Cakes, Price List, Wedding cakes, Get in Touch

I would like to see the page of the full cake menu with the prices.
Signature colours Black, White and Pink

Target Market(s)

My main audience is targeted at women.

Industry/Entity Type

Wedding

Requirements
Must have
• Must look like the link I provided. Please use this as reference.
Nice to have
• Nice to see aspects of my logo, example the butterflies or the paisley design be subtly used around the website.

```html
<!DOCTYPE html>
<html lang="en">
<head>
<meta charset="utf-8">
<title>Velvet Crumbhouse</title>
<link rel="stylesheet" href="https://fonts.googleapis.com/css2?family=Great+Vibes&family=Cabin:wght@400;500;600&display=swap">
<style>
:root{
  --plum:#5a0f33;
  --plum-deep:#3f0822;
  --pink:#c4567f;
  --pink-soft:#e9a7bf;
  --ink:#2b2b2b;
  --grey:#6f6f6f;
  --line:#bdbdbd;
  --white:#ffffff;
  --footer:#262626;
}
*{margin:0;padding:0;box-sizing:border-box}
html,body{width:1200px;height:4528px;overflow:hidden;background:var(--white)}
body{font-family:"Cabin",sans-serif;color:var(--ink);position:relative}
.page{position:relative;width:1200px;height:4528px}
section,header,footer{position:absolute;left:0;width:1200px}
.script{font-family:"Great Vibes",cursive;color:var(--pink);font-weight:400;line-height:1}
.caps{text-transform:uppercase;font-weight:600;letter-spacing:1px;line-height:1}
.photo{position:absolute;border-radius:2px}
p{font-size:15px;line-height:1.55;color:var(--grey)}
.btn{display:inline-block;border:1px solid var(--line);padding:7px 16px;font-size:11px;letter-spacing:1px;text-transform:uppercase;color:var(--grey);background:var(--white)}
.wave{position:absolute;left:0;width:1200px;height:34px;z-index:2}
.wave.top{top:0}
.wave.bottom{bottom:0;transform:scaleY(-1)}

/* Hero */
.hero{top:0;height:558px;background:radial-gradient(ellipse at 30% 40%,#6e1740 0%,var(--plum) 50%,var(--plum-deep) 100%)}
.brand{position:absolute;left:212px;top:0;width:190px;height:92px;background:var(--white);display:flex;align-items:center;justify-content:center;gap:8px;box-shadow:0 2px 6px rgba(0,0,0,.25)}
.brand .mark{width:12px;height:12px;background:var(--pink);border-radius:50%}
.brand span{font-family:"Cabin",sans-serif;font-size:17px;font-weight:500;color:var(--plum)}
.nav{position:absolute;left:592px;top:40px;display:flex;gap:6px}
.nav a{color:var(--white);font-size:13px;text-decoration:none;padding:6px 10px}
.nav a.active{background:var(--pink);border-radius:2px}
.social-top{position:absolute;right:180px;top:8px;display:flex;gap:16px}
.social-top i{width:14px;height:14px;border-radius:50%;background:rgba(255,255,255,.75)}
.hero .welcome{position:absolute;left:232px;top:196px;font-size:76px}
.hero h1{position:absolute;left:232px;top:268px;font-size:44px;color:var(--white);letter-spacing:2px}
.hero p{position:absolute;left:232px;top:330px;width:360px;font-size:13px;color:#e5cdd7}
.hero .more{position:absolute;left:232px;top:456px;font-size:12px;color:var(--white);letter-spacing:1px;text-transform:uppercase}
.hero .cupcake{left:770px;top:70px;width:260px;height:465px;background:radial-gradient(ellipse at 50% 35%,#fbe3ec 0%,#f39ec0 40%,#c7467b 75%,transparent 78%)}
.pager{position:absolute;right:195px;top:492px;display:flex;gap:10px;font-size:11px;color:#d9b8c6}

/* Text blocks */
.block{position:absolute;text-align:center}
.block .script{font-size:64px}
.block h2{font-size:46px;margin-top:-4px;color:var(--ink)}
.block .rule{width:26px;height:2px;background:var(--line);margin:16px auto 18px}
.block p{margin-bottom:14px}

/* Story */
.story{top:558px;height:404px}
.story .block{left:210px;top:60px;width:370px}

/* Bands */
.band{overflow:hidden}
.band .label{position:absolute;left:0;right:0;text-align:center;z-index:1}
.band .label .script{font-size:78px;color:var(--white)}
.band .label .caps{font-size:44px;color:var(--white);margin-top:-6px}
.delights{top:962px;height:390px;background:linear-gradient(90deg,#c79a6a,#6b3c2c 35%,#a35c6a 60%,#e2c3a4)}
.blend{top:1944px;height:390px;background:linear-gradient(90deg,#d8a5ad,#efe3dc 40%,#f5ece4 60%,#c34a5a)}
.special{top:2748px;height:385px;background:linear-gradient(90deg,#e6c24a,#e3437a 20%,#7a3fa0 40%,#f0a03a 60%,#e86aa0 80%,#8cc24a)}
.order{top:3604px;height:390px;background:linear-gradient(90deg,#2e6f8a,#7ab3c9 35%,#c7567f 60%,#3b8aa3)}

/* Cakes */
.cakes{top:1352px;height:592px}
.cakes .block{left:625px;top:60px;width:470px}
.cakes p{font-size:14px}

/* Promise */
.promise{top:2334px;height:414px}
.promise .block{left:200px;top:66px;width:400px}

/* Wedding */
.wedding{top:3133px;height:471px}
.wedding .block{left:630px;top:60px;width:460px}
.wedding .lead{color:var(--ink);font-weight:600;font-size:15px}

/* Contact */
.contact{top:3994px;height:360px}
.contact .block{left:200px;top:46px;width:320px}
.contact p{font-size:14px}
.form{position:absolute;left:634px;top:40px;width:432px}
.form .row{display:flex;gap:12px;margin-bottom:12px}
.field{flex:1;height:34px;border:1px solid #d6d6d6;font-size:11px;color:#9a9a9a;padding:9px 10px}
.field.msg{height:94px}
.send{height:32px;background:var(--pink);color:var(--white);font-size:13px;text-align:center;line-height:32px}

/* Footer */
.footer{top:4354px;height:174px;background:var(--footer);text-align:center;color:#bdbdbd}
.footer .icons{position:absolute;left:0;right:0;top:48px;display:flex;justify-content:center;gap:10px}
.footer .icons i{width:26px;height:26px;border-radius:50%;background:var(--pink)}
.footer .copy{position:absolute;left:0;right:0;top:96px;font-size:12px}
.footer .links{position:absolute;left:0;right:0;top:124px;font-size:12px}
</style>
</head>
<body>
<div class="page">

<svg width="0" height="0" style="position:absolute">
  <defs>
    <pattern id="scallop" width="46" height="34" patternUnits="userSpaceOnUse">
      <rect width="46" height="12" fill="#fff"/>
      <ellipse cx="23" cy="12" rx="26" ry="12" fill="#fff"/>
    </pattern>
    <pattern id="scallop-dark" width="46" height="34" patternUnits="userSpaceOnUse">
      <rect width="46" height="12" fill="#262626"/>
      <ellipse cx="23" cy="12" rx="26" ry="12" fill="#262626"/>
    </pattern>
  </defs>
</svg>

<header class="hero">
  <div class="brand"><i class="mark"></i><span>Velvet Crumbhouse</span></div>
  <nav class="nav">
    <a class="active">Home</a><a>Our Story</a><a>Our Cakes</a><a>Price List</a><a>Wedding Cakes</a><a>Get In Touch</a>
  </nav>
  <div class="social-top"><i></i><i></i><i></i><i></i></div>
  <div class="welcome script">Welcome</div>
  <h1 class="caps">Velvet Crumbhouse</h1>
  <p>Handmade cupcakes and celebration cakes baked fresh in our home kitchen, finished by hand with care for every detail and every guest at your table.</p>
  <div class="more">View all cupcakes →</div>
  <div class="photo cupcake" role="img" aria-label="Pink frosted cupcake in a pink paper case"></div>
  <div class="pager"><span>1</span><span>2</span><span>3</span></div>
  <svg class="wave bottom" viewBox="0 0 1200 34" preserveAspectRatio="none"><rect width="1200" height="34" fill="url(#scallop)"/></svg>
</header>

<section class="story">
  <div class="block">
    <div class="script">Discover</div>
    <h2 class="caps">Our Story</h2>
    <div class="rule"></div>
    <p>Velvet Crumbhouse began in a small family kitchen with a love of baking and a wish to make every celebration sweeter. Our cakes are baked to order, decorated by hand and made to be remembered.</p>
    <span class="btn">About us</span>
  </div>
  <div class="photo" style="left:612px;top:58px;width:180px;height:262px;background:linear-gradient(160deg,#f6d9df,#e9a6b3 50%,#c98a6c)" role="img" aria-label="Cupcakes topped with pink frosting hearts"></div>
  <div class="photo" style="left:800px;top:58px;width:176px;height:262px;background:linear-gradient(160deg,#bfe4f2,#3fa9d8 50%,#e7b9c8)" role="img" aria-label="Cupcakes with blue swirled frosting"></div>
</section>

<section class="band delights" role="img" aria-label="Close-up of frosted cupcakes with chocolate and pink icing">
  <svg class="wave top" viewBox="0 0 1200 34" preserveAspectRatio="none"><rect width="1200" height="34" fill="url(#scallop)"/></svg>
  <div class="label" style="top:150px"><div class="script">Tasteful</div><div class="caps">Delights</div></div>
  <svg class="wave bottom" viewBox="0 0 1200 34" preserveAspectRatio="none"><rect width="1200" height="34" fill="url(#scallop)"/></svg>
</section>

<section class="cakes">
  <div class="photo" style="left:160px;top:62px;width:202px;height:226px;background:linear-gradient(160deg,#cfe9f3,#f2a2bf 55%,#d37a96)" role="img" aria-label="Cupcake with pink rose frosting"></div>
  <div class="photo" style="left:372px;top:62px;width:204px;height:226px;background:linear-gradient(160deg,#d9eff7,#49b4e0 55%,#2f8fbf)" role="img" aria-label="Row of blue frosted cupcakes"></div>
  <div class="photo" style="left:160px;top:298px;width:202px;height:228px;background:linear-gradient(160deg,#fbe0ea,#ec80a8 55%,#c24c7b)" role="img" aria-label="Cupcake with bright pink swirl frosting"></div>
  <div class="photo" style="left:372px;top:298px;width:204px;height:228px;background:linear-gradient(160deg,#f3e4e6,#e6a6b0 55%,#c98a6c)" role="img" aria-label="Cupcakes decorated with pink hearts"></div>
  <div class="block">
    <div class="script">Discover</div>
    <h2 class="caps">Our Cakes</h2>
    <div class="rule"></div>
    <p>Velvet Crumbhouse offers a wide range of cakes and cupcakes for every occasion, from birthdays and christenings to baby showers and anniversaries. Each cake is baked from scratch with quality ingredients and decorated by hand to suit your theme, colours and taste.</p>
    <p>Looking for something more creative? Tell us about your idea and we will design a cake that is truly yours, with flavours and finishes chosen together.</p>
    <span class="btn">View the full cake menu</span>
  </div>
</section>

<section class="band blend" role="img" aria-label="Cupcakes with cream frosting and red sugared berries">
  <svg class="wave top" viewBox="0 0 1200 34" preserveAspectRatio="none"><rect width="1200" height="34" fill="url(#scallop)"/></svg>
  <div class="label" style="top:150px"><div class="script">The Perfect</div><div class="caps">Blend</div></div>
  <svg class="wave bottom" viewBox="0 0 1200 34" preserveAspectRatio="none"><rect width="1200" height="34" fill="url(#scallop)"/></svg>
</section>

<section class="promise">
  <div class="block">
    <div class="script">Discover</div>
    <h2 class="caps">Our Promise</h2>
    <div class="rule"></div>
    <p>Every cake leaves our kitchen freshly baked, carefully finished and delivered on time. We use only fine ingredients, listen closely to your wishes and never compromise on taste or presentation.</p>
    <span class="btn">Our promise</span>
  </div>
  <div class="photo" style="left:612px;top:66px;width:176px;height:286px;background:linear-gradient(160deg,#f7e6ea,#f2b8c6 50%,#d9465f)" role="img" aria-label="Cupcake topped with a red heart"></div>
  <div class="photo" style="left:800px;top:66px;width:176px;height:286px;background:linear-gradient(160deg,#f6a3c4,#ef7fae 50%,#f4d6df)" role="img" aria-label="Cupcake with heart-shaped candles"></div>
</section>

<section class="band special" role="img" aria-label="Rows of cupcakes with rainbow coloured frosting">
  <svg class="wave top" viewBox="0 0 1200 34" preserveAspectRatio="none"><rect width="1200" height="34" fill="url(#scallop)"/></svg>
  <div class="label" style="top:140px"><div class="script">Discover</div><div class="caps">Your Special Day</div></div>
  <svg class="wave bottom" viewBox="0 0 1200 34" preserveAspectRatio="none"><rect width="1200" height="34" fill="url(#scallop)"/></svg>
</section>

<section class="wedding">
  <div class="photo" style="left:160px;top:66px;width:200px;height:350px;background:linear-gradient(170deg,#5b4a42,#a98a7a 50%,#3a2d28)" role="img" aria-label="Tiered wedding cupcake stand"></div>
  <div class="photo" style="left:372px;top:66px;width:204px;height:170px;background:linear-gradient(160deg,#f1f1f1,#c9c9c9 60%,#8d8d8d)" role="img" aria-label="Cupcake presented in a teacup"></div>
  <div class="photo" style="left:372px;top:246px;width:204px;height:170px;background:linear-gradient(160deg,#f6e4ea,#e4a4b9 55%,#7a4a4a)" role="img" aria-label="Wedding cupcakes on a cake stand"></div>
  <div class="block">
    <div class="script">Discover</div>
    <h2 class="caps">Wedding Cakes</h2>
    <div class="rule"></div>
    <p class="lead">Velvet Crumbhouse would be delighted to be part<br>of your wedding celebrations.</p>
    <p>We like to meet every couple to talk through their ideas, so that we can create a cake that reflects your style, your venue and your story.</p>
    <p>Consultations are held in our studio by appointment, where you can taste a selection of flavours and see sample designs. Please contact us early to check availability for your date.</p>
  </div>
</section>

<section class="band order" role="img" aria-label="Cupcakes with colourful piped frosting on a blue background">
  <svg class="wave top" viewBox="0 0 1200 34" preserveAspectRatio="none"><rect width="1200" height="34" fill="url(#scallop)"/></svg>
  <div class="label" style="top:148px"><div class="script">Make</div><div class="caps">An Order</div></div>
  <svg class="wave bottom" viewBox="0 0 1200 34" preserveAspectRatio="none"><rect width="1200" height="34" fill="url(#scallop)"/></svg>
</section>

<section class="contact">
  <div class="block">
    <div class="script">Get</div>
    <h2 class="caps">In Touch</h2>
    <div class="rule"></div>
    <p>We would love to hear from you. Send us a message about your occasion, date and ideas, and we will reply within two working days with details and pricing.</p>
  </div>
  <div class="form">
    <div class="row"><div class="field">First Name</div><div class="field">Last Name</div></div>
    <div class="row"><div class="field">Email</div></div>
    <div class="row"><div class="field msg">Message</div></div>
    <div class="send">Send Message</div>
  </div>
</section>

<footer class="footer">
  <svg class="wave top" viewBox="0 0 1200 34" preserveAspectRatio="none" style="top:-33px;transform:scaleY(-1)"><rect width="1200" height="34" fill="url(#scallop-dark)"/></svg>
  <div class="icons"><i></i><i></i><i></i><i></i><i></i></div>
  <div class="copy">Copyright © Velvet Crumbhouse 2014 &nbsp;|&nbsp; 14 Maple Row, Dubai &nbsp;|&nbsp; Tel: +44 00 1234 567</div>
  <div class="links">Privacy Policy &nbsp;|&nbsp; Contact The Team</div>
</footer>

</div>
</body>
</html>
```